Property Management Company

We are looking for a sharp/modern business card design for a property management company.
We have included what should be on the business card down below in business card details.
Target Market(s)
Commercial properties, Home Owners
Industry/Entity Type
Business
Contact Information for Business Card
Name: Dale Orsino | Owner
Business Name : Kestrel Yards
Slogan : A Smarter Choice
Phone : 555.304.8862
Website: www.kestrelyards.example
E-Mail : dale@kestrelyards.example
Our Services are Commercial & Residential
-Asphalt Maintenance
-Snow Management
-Landscaping
-Blacktop
Free Estimates
Free parking lot cleanup & restripe with snow removal contract
Look and feel

```html
<!DOCTYPE html>
<html lang="en">
<head>
<meta charset="utf-8">
<title>Kestrel Yards — Business Card</title>
<link rel="stylesheet" href="https://fonts.googleapis.com/css2?family=Josefin+Sans:wght@300;400;700&display=swap">
<style>
  :root {
    --navy: #1c2551;
    --red: #be1e2d;
    --white: #ffffff;
    --page: #ffffff;
    --text-font: "Josefin Sans", Arial, sans-serif;
  }
  * { margin: 0; padding: 0; box-sizing: border-box; }
  html, body { width: 675px; height: 1200px; overflow: hidden; background: var(--page); }
  body { position: relative; font-family: var(--text-font); color: var(--white); }

  .card {
    position: absolute; left: 72px; width: 516px;
    background: var(--navy); overflow: hidden;
  }
  .card--front { top: 12px; height: 292px; }
  .card--back { top: 308px; height: 295px; }

  .star { position: absolute; display: block; }
  .star polygon { fill: var(--white); }

  .brand-name {
    position: absolute; left: 0; width: 100%; text-align: center;
    font-weight: 700; color: var(--navy); text-transform: uppercase;
    letter-spacing: 1px; line-height: 1.05;
  }
  .card--front .brand-name { top: 120px; font-size: 22px; }
  .card--back .brand-name { top: 7px; font-size: 16px; }

  .service-band {
    position: absolute; left: 0; bottom: 0; width: 100%; height: 36px;
  }
  .service-band svg { position: absolute; inset: 0; }
  .service-band .band-line { fill: var(--white); }
  .service-band .band-fill { fill: var(--red); }
  .service-band p {
    position: absolute; left: 28px; right: 8px; bottom: 7px; font-size: 5.4px; font-weight: 400;
    white-space: nowrap; line-height: 1;
  }
  .service-band strong { font-weight: 400; margin-right: 6px; }

  .company { position: absolute; top: 114px; left: 0; width: 100%; text-align: center; color: var(--white); }
  .company-name { font-size: 12px; font-weight: 400; letter-spacing: 0.5px; text-transform: uppercase; line-height: 1.1; }
  .company-slogan { font-size: 6px; letter-spacing: 0.6px; text-transform: uppercase; margin-top: 1px; }

  .name-band {
    position: absolute; top: 144px; left: 0; width: 100%; height: 40px;
    background: var(--red); border-top: 1px solid var(--white); border-bottom: 1px solid var(--white);
    text-align: center;
  }
  .person-name { font-size: 17px; font-weight: 300; letter-spacing: 0.5px; margin-top: 9px; line-height: 1; text-transform: uppercase; }
  .person-role { font-size: 6px; letter-spacing: 5px; margin-top: 2px; text-transform: uppercase; }

  .contact-strip {
    position: absolute; left: 0; top: 197px; width: 28px; height: 98px; background: var(--white);
  }
  .contact-strip svg { position: absolute; left: 7px; width: 14px; height: 14px; }
  .contact-strip .icon-phone { top: 13px; }
  .contact-strip .icon-mail { top: 32px; }
  .contact-strip .icon-web { top: 51px; }
  .contact-list { position: absolute; left: 38px; top: 212px; list-style: none; font-size: 11px; font-weight: 300; }
  .contact-list li { height: 19px; }

  .services { position: absolute; right: 6px; top: 199px; text-align: right; }
  .services h2 { font-size: 6.6px; font-weight: 400; text-transform: uppercase; margin-bottom: 4px; }
  .services ul { list-style: none; font-size: 5.6px; font-weight: 300; }
  .services li { height: 12.3px; }
  .services li::before { content: "• "; }
</style>
</head>
<body>

<section class="card card--front" aria-label="Card front">
  <svg class="star" style="left:133px;top:28px;width:250px;height:250px" viewBox="-1 -1 2 2" aria-hidden="true">
    <polygon points="0,-1 .225,-.309 .951,-.309 .363,.118 .588,.809 0,.382 -.588,.809 -.363,.118 -.951,-.309 -.225,-.309"/>
  </svg>
  <div class="brand-name">Kestrel<br>Yards</div>

  <div class="service-band">
    <svg viewBox="0 0 516 36" preserveAspectRatio="none" aria-hidden="true">
      <polygon class="band-line" points="0,14 516,4 516,36 0,36"/>
      <polygon class="band-fill" points="0,16 516,6 516,36 0,36"/>
    </svg>
    <p><strong>COMMERCIAL &amp; RESIDENTIAL :</strong> • Asphalt Maintenance • Snow Management • Landscaping • Blacktop Free Estimates • Free parking lot cleanup • Restripe with snow removal contract</p>
  </div>
</section>

<section class="card card--back" aria-label="Card back">
  <svg class="star" style="left:155px;top:-69px;width:206px;height:206px" viewBox="-1 -1 2 2" aria-hidden="true">
    <polygon points="0,-1 .225,-.309 .951,-.309 .363,.118 .588,.809 0,.382 -.588,.809 -.363,.118 -.951,-.309 -.225,-.309"/>
  </svg>
  <div class="brand-name">Kestrel<br>Yards</div>

  <div class="company">
    <p class="company-name">Kestrel Yards</p>
    <p class="company-slogan">“A Smarter Choice”</p>
  </div>

  <div class="name-band">
    <p class="person-name">Dale Orsino</p>
    <p class="person-role">Owner</p>
  </div>

  <div class="contact-strip" aria-hidden="true">
    <svg class="icon-phone" viewBox="0 0 14 14"><circle cx="7" cy="7" r="7" fill="#1c2551"/><path d="M4.5 3.5h1.6l.6 2-1 .8a5 5 0 0 0 2.4 2.4l.8-1 2 .6v1.6c0 .4-.4.7-.8.7A6.5 6.5 0 0 1 3.8 4.3c0-.4.3-.8.7-.8z" fill="#fff"/></svg>
    <svg class="icon-mail" viewBox="0 0 14 14"><circle cx="7" cy="7" r="7" fill="#1c2551"/><rect x="3.5" y="4.5" width="7" height="5" fill="#fff"/><path d="M3.5 4.5 7 7.3l3.5-2.8" fill="none" stroke="#1c2551" stroke-width=".8"/></svg>
    <svg class="icon-web" viewBox="0 0 14 14"><circle cx="7" cy="7" r="7" fill="#1c2551"/><circle cx="4.3" cy="7" r=".9" fill="#fff"/><circle cx="7" cy="7" r=".9" fill="#fff"/><circle cx="9.7" cy="7" r=".9" fill="#fff"/></svg>
  </div>
  <ul class="contact-list">
    <li>555.304.8862</li>
    <li>dale@kestrelyards.example</li>
    <li>www.kestrelyards.example</li>
  </ul>

  <div class="services">
    <h2>Commercial &amp; Residential</h2>
    <ul>
      <li>Asphalt Maintenance</li>
      <li>Snow Management</li>
      <li>Landscaping</li>
      <li>Backtop Free Estimates</li>
      <li>Free parking lot cleanup</li>
      <li>Restripe with snow removal contract</li>
    </ul>
  </div>
</section>

</body>
</html>
```